Flyer-Design für Touroperator/Eventveranstalter
Zielgruppe
Die Zielgruppe sind ausschliesslich Frauen zwischen 25 und 55 Jahren.
Meine Firma organisiert unvergessliche Städtetrips mit Programm vor Ort.
Städte in Osteuropa wobei derzeit nur im Programm Warschau und Prag.
Mit dem Flyer soll die Sommertour Warschau beworben werden.
Die Städtetrips sind höherer Standard und exklusiv.
Aufgabenstellung
Der Flyer soll nicht zu groß sein z.B. DIN A6 sein und Vorder- und Rückseite haben.
Jedenfalls soll der Flyer handlich bleiben, so dass er sich z.B. als Beilage in Einkaufstüten eignet etc.
Dafür muss der beigefügte Text gekürzt werden. Mein Entwurf hat zu viel Text aber ich weiss nicht, wieviel auf einen Flyer passt. Außerdem muss der Flyer unbedingt mein Logo und meine Firmenangaben beinhalten.
Der Flyer soll das beigefügte Frauengruppenfoto beinhalten und ein Foto aus den beigefügten Warschau Fotos.
Vielleicht kann man auch mehrere Fotos zusammen schneiden.

```html
<!DOCTYPE html>
<html lang="de">
<head>
<meta charset="utf-8">
<title>Lunaria Tours – Flyer Sommertour Warschau</title>
<link href="https://fonts.googleapis.com/css2?family=Fira+Sans:wght@400;500;600;700;800&family=Great+Vibes&display=swap" rel="stylesheet">
<style>
:root{
  --stage:#525252;
  --cream:#efe3d4;
  --cream-light:#faf4ec;
  --magenta:#b5127a;
  --gold:#a8864a;
  --navy:#1f2a64;
  --ink:#333333;
  --white:#ffffff;
}
*{margin:0;padding:0;box-sizing:border-box}
html,body{width:1200px;height:852px;overflow:hidden;background:var(--stage);font-family:"Fira Sans",Arial,sans-serif}
.canvas{position:relative;width:1200px;height:852px}
.page{position:absolute;top:52px;width:532px;height:749px;overflow:hidden;
  background:
   radial-gradient(circle at 12% 10%,rgba(255,255,255,.8) 0 22px,transparent 24px),
   radial-gradient(circle at 88% 30%,rgba(255,255,255,.6) 0 30px,transparent 32px),
   radial-gradient(circle at 20% 55%,rgba(255,255,255,.5) 0 26px,transparent 28px),
   radial-gradient(circle at 75% 85%,rgba(255,255,255,.55) 0 34px,transparent 36px),
   radial-gradient(ellipse at 50% 45%,var(--cream-light),var(--cream));}
.page--front{left:58px}
.page--back{left:620px}
.abs{position:absolute}
.brand{position:absolute;display:flex;align-items:center;justify-content:center;
  border:1.5px solid var(--gold);color:var(--gold);font-weight:600;text-align:center;line-height:1.1}
.brand--front{left:55px;top:37px;width:98px;height:101px;font-size:18px}
.brand--back{left:26px;top:618px;width:106px;height:84px;font-size:18px}
.banner{position:absolute;left:177px;top:41px;width:355px;height:99px;background:var(--magenta);color:var(--white);font-weight:700;padding:12px 0 0 18px}
.banner__line1{font-size:22.5px;letter-spacing:-.4px}
.banner__line2{font-size:20.5px;line-height:22px;margin-top:7px;padding-left:2px}
.scene{position:absolute;left:0;top:0}
.polaroid{position:absolute;background:var(--white);padding:8px;box-shadow:0 3px 10px rgba(0,0,0,.3)}
.polaroid__photo{width:100%;height:100%}
.tagline{right:28px;top:535px;font-family:"Great Vibes",cursive;font-size:24px;line-height:30px;color:var(--navy);white-space:nowrap;text-align:right}
.tagline .star{color:var(--magenta);font-size:26px}
.pitch{right:27px;top:578px;text-align:right;color:var(--magenta);font-weight:700;font-size:22px;line-height:24.5px;white-space:nowrap}
.claim{right:30px;top:680px;text-align:right;color:var(--navy);font-weight:700;font-size:20px;line-height:22px;letter-spacing:-.3px}
.headline{left:0;width:532px;top:25px;text-align:center;color:var(--ink);font-weight:700;font-size:25.5px;line-height:25px;letter-spacing:-.3px}
.tour-box{left:55px;top:85px;width:429px;height:140px;background:var(--magenta);color:var(--white)}
.tour-box__title{position:absolute;left:33px;top:11px;font-weight:700;font-size:22.5px;letter-spacing:-.2px}
.tour-list{position:absolute;list-style:none;font-size:15.8px;font-weight:500;line-height:20px;top:44px;white-space:nowrap}
.tour-list--a{left:33px}.tour-list--b{left:204px}
.highlights-tag{left:57px;top:233px;width:23px;height:87px;background:var(--magenta);color:var(--white);
  font-size:11px;font-weight:700;writing-mode:vertical-rl;transform:rotate(180deg);display:flex;align-items:center;justify-content:center;letter-spacing:.5px}
.highlights{left:83px;top:240px;list-style:none;font-size:14.6px;line-height:20.3px;color:var(--ink);white-space:nowrap}
.rule{position:absolute;height:1px;background:#666}
.contact{left:148px;top:612px;color:var(--ink);white-space:nowrap}
.contact__mail{font-size:16.5px;font-weight:500;line-height:20px}
.contact__phone{font-size:16px;font-weight:500;line-height:22px}
.contact__phone b{font-size:21px;font-weight:700}
.contact__company{font-size:14px;margin-top:5px;line-height:17px}
.url{left:0;width:532px;top:685px;text-align:center;color:var(--magenta);font-weight:800;font-size:41px;letter-spacing:-.3px}
.format{right:55px;top:816px;color:var(--white);font-weight:700;font-size:15px}
</style>
</head>
<body>
<div class="canvas">

  <section class="page page--front">
    <svg class="scene" width="532" height="749" viewBox="0 0 532 749">
      <defs>
        <linearGradient id="groupTone" x1="0" y1="0" x2="0" y2="1">
          <stop offset="0" stop-color="#c9a888"/>
          <stop offset=".5" stop-color="#b98a6e"/>
          <stop offset=".85" stop-color="#e9dccd"/>
          <stop offset="1" stop-color="#f4ebe0" stop-opacity="0"/>
        </linearGradient>
      </defs>
      <path role="img" aria-label="Foto: drei lachende Freundinnen mit bunten Sonnenbrillen in einer Altstadtgasse"
            d="M0 340 Q230 205 532 232 L532 600 L0 600 Z" fill="url(#groupTone)"/>
      <path d="M0 345 Q230 195 532 225 L532 240 Q240 215 0 358 Z" fill="#d8c5a8"/>
      <path d="M0 322 Q230 180 532 202 L532 207 Q235 188 0 328 Z" fill="var(--magenta)"/>
    </svg>

    <div class="brand brand--front">Lunaria<br>Tours</div>

    <div class="banner">
      <div class="banner__line1">WIR BRINGEN FRAUEN AUF TOUR</div>
      <div class="banner__line2">WIR BRINGEN SCHWUNG<br>IN EURE MÄDELSTOUR!</div>
    </div>

    <div class="polaroid" style="left:30px;top:420px;width:205px;height:190px;transform:rotate(-5deg)">
      <div class="polaroid__photo" role="img" aria-label="Foto: Skyline von Warschau bei Nacht" style="background:linear-gradient(160deg,#3b6fb0,#1b2f5e 60%,#d09a4a)"></div>
    </div>
    <div class="polaroid" style="left:38px;top:568px;width:182px;height:168px;transform:rotate(-6deg)">
      <div class="polaroid__photo" role="img" aria-label="Foto: Weichselufer mit Sandstrand in der Abenddämmerung" style="background:linear-gradient(180deg,#2f5f9c,#24457a 55%,#cfc6b8)"></div>
    </div>

    <div class="abs tagline">Sich ganz wie ein <span class="star">STAR</span> fühlen</div>
    <div class="abs pitch">Wir arrangieren für Euch<br>einen unvergesslichen<br>Kurztrip nach Warschau.</div>
    <div class="abs claim">MALLE IST OUT,<br>WARSCHAU IST IN</div>
  </section>

  <section class="page page--back">
    <div class="abs headline">DIE PERFEKTE PLANUNG FÜR EURE<br>MÄDELSTOUR MIT LUNARIA TOURS!</div>

    <div class="abs tour-box">
      <div class="tour-box__title">UNSERE SOMMERTOUR WARSCHAU</div>
      <ul class="tour-list tour-list--a">
        <li>• Retro-Bus Tour</li><li>• Altstadtbummel</li><li>• Shopping Tour</li><li>• Natur pur - Parks</li>
      </ul>
      <ul class="tour-list tour-list--b">
        <li>• Bootsfahrt</li><li>• Barbecue am Strand</li><li>• Nightlife mit Bar-Hopping</li><li>• Essen in Top-Restaurant</li>
      </ul>
    </div>

    <div class="abs highlights-tag">HIGHLIGHTS</div>
    <ul class="abs highlights">
      <li>• Chauffeur bringt Euch zu Eurem Hotel.</li>
      <li>• Im Zimmer erwartet Euch eine Überraschung.</li>
      <li>• Programm wird nach Euren Interessen angepasst.</li>
      <li>• Schlecht Wetter Programm inklusive (Wellness, Kosmetik).</li>
    </ul>
    <div class="rule" style="left:83px;top:325px;width:401px"></div>

    <div class="polaroid" style="left:8px;top:330px;width:212px;height:250px;transform:rotate(4deg)">
      <div class="polaroid__photo" role="img" aria-label="Foto: Kulturpalast und Hochhäuser in Warschau" style="background:linear-gradient(180deg,#a9b9cf,#8a8e8a 55%,#6b6a5a)"></div>
    </div>
    <div class="polaroid" style="left:226px;top:332px;width:212px;height:224px;transform:rotate(-3deg)">
      <div class="polaroid__photo" role="img" aria-label="Foto: Frauengruppe vor einem gelben Retro-Bus" style="background:linear-gradient(180deg,#d8d6d0,#c9b13a 45%,#3a3a3a 70%,#bdbab4)"></div>
    </div>
    <div class="polaroid" style="left:360px;top:428px;width:172px;height:200px;transform:rotate(10deg)">
      <div class="polaroid__photo" role="img" aria-label="Foto: Stadion und Sandstrand an der Weichsel" style="background:linear-gradient(180deg,#dfe3e6,#5f8a4a 45%,#c9b28e)"></div>
    </div>

    <div class="brand brand--back">Lunaria<br>Tours</div>

    <div class="abs contact">
      <div class="contact__mail">ANFRAGEN: info@lunariatours.de</div>
      <div class="contact__phone">What’s app <b>0171-5550123</b></div>
      <div class="contact__company"><b>Greta &amp; Co</b> &nbsp;|&nbsp; Travel and Events GmbH,<br>Lindenweg 14, 50667 Köln</div>
    </div>
    <div class="rule" style="left:148px;top:655px;width:336px"></div>

    <div class="abs url">www.lunariatours.de</div>
  </section>

  <div class="abs format">DIN A6</div>
</div>
</body>
</html>
```